New (old) Business Card Design Project

I would like to purchase a customized version of a design you have previously submitted - https://www.artmarketly.example/design/7305126

I like the card above, and would like to use the same design, jus with my business name, HARLOWAY ASSET ADVISORS. I like the colors in the card above, as well as the font. The other side will have my name, company name, address, phone, email, website, plus disclosure text I will provide.

Target Market(s)

wealthy families

Industry/Entity Type

Financial Services

Contact Information for Business Card

logo on one side, on other my name, company, address, phone, email, website, disclosure language I will provide.

Colors

Designer to choose colors to be used in the design.

Requirements
Must have
• colors: Deep blue and white
Nice to have
• Please see the items I have uploaded, below.
Should not have
• Cheap, tacky look.

```html
<!DOCTYPE html>
<html lang="en">
<head>
<meta charset="utf-8">
<title>Harloway Asset Advisors — Business Card</title>
<link rel="stylesheet" href="https://fonts.googleapis.com/css2?family=Cinzel:wght@400;500&family=Arimo:wght@400&display=swap">
<style>
  :root {
    --navy: #0c1f5e;
    --navy-text: #1b2a66;
    --paper: #f3f3f4;
    --backdrop: #e4e4e6;
    --ink: #3a3a3d;
    --rule: #6a6a70;
    --tagline-rule: #8fa6d8;
  }
  * { margin: 0; padding: 0; box-sizing: border-box; }
  html, body {
    width: 1200px; height: 726px; overflow: hidden;
    background: var(--backdrop);
  }
  .sheet {
    position: relative; width: 1200px; height: 726px;
    display: flex; align-items: center; justify-content: center; gap: 40px;
  }
  .card {
    position: relative; width: 520px; height: 297px;
    box-shadow: 0 6px 18px rgba(0,0,0,0.14);
    overflow: hidden;
  }

  /* Front */
  .card-front {
    background: var(--navy);
    color: #fff;
    display: flex; flex-direction: column; align-items: center; justify-content: center;
  }
  .company-name {
    font-family: "Cinzel", serif;
    font-weight: 400;
    font-size: 27px;
    letter-spacing: 2px;
    color: #fff;
    white-space: nowrap;
    margin-top: 18px;
  }
  .tagline {
    display: flex; align-items: center; gap: 26px;
    margin-top: 34px;
    font-family: "Cinzel", serif;
    font-size: 11.5px;
    letter-spacing: 1.5px;
    color: #fff;
  }
  .tagline .sep {
    width: 1px; height: 12px; background: var(--tagline-rule);
  }

  /* Back */
  .card-back {
    background: var(--paper);
  }
  .card-back .band {
    position: absolute; left: 0; right: 0; bottom: 0; height: 12px;
    background: var(--navy);
  }
  .identity {
    position: absolute; right: 296px; top: 128px;
    text-align: right;
  }
  .person-name {
    font-family: "Cinzel", serif;
    font-size: 19px;
    color: var(--navy-text);
    letter-spacing: 0.5px;
    white-space: nowrap;
  }
  .person-title {
    font-family: "Arimo", sans-serif;
    font-size: 12px;
    color: var(--ink);
    margin-top: 2px;
  }
  .divider {
    position: absolute; left: 238px; top: 100px;
    width: 1px; height: 88px; background: var(--rule);
  }
  .contact {
    position: absolute; left: 252px; top: 100px;
    list-style: none;
    font-family: "Arimo", sans-serif;
    font-size: 11.5px;
    color: var(--ink);
  }
  .contact li {
    display: flex; align-items: center; gap: 8px;
    height: 15px; margin-bottom: 1px;
    white-space: nowrap;
  }
  .contact svg { width: 10px; height: 10px; flex: none; }
  .contact .accent { color: var(--navy-text); }
</style>
</head>
<body>
<main class="sheet">

  <section class="card card-front" aria-label="Card front">
    <div class="company-name">HARLOWAY ASSET ADVISORS</div>
    <div class="tagline">
      <span>PLAN</span><span class="sep"></span>
      <span>SECURE</span><span class="sep"></span>
      <span>SUSTAIN</span>
    </div>
  </section>

  <section class="card card-back" aria-label="Card back">
    <div class="identity">
      <div class="person-name">ELLIOT HARLOWAY</div>
      <div class="person-title">Managing Director</div>
    </div>
    <div class="divider"></div>
    <ul class="contact">
      <li>
        <svg viewBox="0 0 10 10" aria-hidden="true"><circle cx="5" cy="5" r="4.3" fill="none" stroke="var(--ink)" stroke-width="1"/><path d="M3.4 3.2 L4.2 3 L4.6 4.1 L4.1 4.5 Q4.6 5.5 5.5 5.9 L5.9 5.4 L7 5.8 L6.8 6.6 Q4.2 6.8 3.4 3.2Z" fill="var(--ink)"/></svg>
        <span>555 0140 2286</span>
      </li>
      <li>
        <svg viewBox="0 0 10 10" aria-hidden="true"><rect x="3" y="1" width="4" height="2.5" fill="none" stroke="var(--ink)" stroke-width="0.9"/><rect x="1" y="3.5" width="8" height="3.5" rx="0.6" fill="var(--ink)"/><rect x="3" y="6" width="4" height="3" fill="#fff" stroke="var(--ink)" stroke-width="0.9"/></svg>
        <span>555 0140 2287</span>
      </li>
      <li>
        <svg viewBox="0 0 10 10" aria-hidden="true"><rect x="0.8" y="2" width="8.4" height="6" fill="none" stroke="var(--ink)" stroke-width="0.9"/><path d="M0.8 2 L5 5.4 L9.2 2" fill="none" stroke="var(--ink)" stroke-width="0.9"/></svg>
        <span>elliot@harlowayadvisors.com</span>
      </li>
      <li>
        <svg viewBox="0 0 10 10" aria-hidden="true"><circle cx="5" cy="5" r="4.2" fill="none" stroke="var(--ink)" stroke-width="0.9"/><ellipse cx="5" cy="5" rx="1.8" ry="4.2" fill="none" stroke="var(--ink)" stroke-width="0.8"/><path d="M0.8 5 H9.2" stroke="var(--ink)" stroke-width="0.8"/></svg>
        <span>www.<span class="accent">harloway</span>advisors.com</span>
      </li>
    </ul>
    <div class="band"></div>
  </section>

</main>
</body>
</html>
```